label update for bottle change

The goal is to adapt the label's design and shape to the new bottle, maintaining its defining elements such as the font, vertical name, company logo, background pattern, and color. The new design should not be identical to the old one, but rather an evolution of it. The gold stripe on the bottom is not mandatory, but the writing "BASSANO DEL GRAPPA / EST. 1886" must be retained, slightly enlarged.

The font name is: Brandon Text

```html
<!DOCTYPE html>
<html lang="it">
<head>
<meta charset="utf-8">
<title>Carciofo – Amaro di carattere</title>
<link rel="stylesheet" href="https://fonts.googleapis.com/css2?family=Fira+Sans+Condensed:wght@600;700&family=Montserrat:wght@500;600;800&display=swap">
<style>
  :root {
    --plum: #4f2a55;
    --plum-deep: #3f2045;
    --plum-light: #5d3463;
    --ivory: #f6f1ea;
    --gold: #8c6c3c;
    --gold-light: #a2824d;
    --leaf: #7f9e52;
    --leaf-dark: #4d6a34;
    --bud: #8e2e4e;
  }
  * { margin: 0; padding: 0; box-sizing: border-box; }
  html, body { width: 900px; height: 1200px; overflow: hidden; background: var(--plum-deep); }
  .label {
    position: relative;
    width: 900px;
    height: 1200px;
    overflow: hidden;
    background: linear-gradient(180deg, var(--plum-light) 0%, var(--plum) 45%, var(--plum-deep) 100%);
    color: var(--ivory);
  }
  .maker {
    position: absolute;
    right: 48px;
    top: 52px;
    text-align: right;
    font-family: "Fira Sans Condensed", sans-serif;
    font-weight: 700;
    line-height: 1;
  }
  .maker__line { display: block; font-size: 55px; letter-spacing: 0.5px; }
  .maker__name { display: block; font-size: 80px; margin-top: 10px; }
  .tagline, .product-name {
    position: absolute;
    writing-mode: vertical-rl;
    transform: rotate(180deg);
    white-space: nowrap;
    line-height: 1;
    font-family: "Montserrat", sans-serif;
  }
  .tagline {
    left: 148px;
    bottom: 268px;
    font-size: 46px;
    font-weight: 600;
    letter-spacing: 5px;
  }
  .product-name {
    left: 222px;
    bottom: 148px;
    font-size: 140px;
    font-weight: 800;
    letter-spacing: 1px;
  }
  .artichoke {
    position: absolute;
    left: 355px;
    top: 230px;
    width: 545px;
    height: 864px;
  }
  .origin-band {
    position: absolute;
    left: 0;
    bottom: 0;
    width: 900px;
    height: 106px;
    background: linear-gradient(180deg, var(--gold-light), var(--gold));
    display: flex;
    align-items: center;
    padding-left: 145px;
  }
  .origin-band__text {
    font-family: "Montserrat", sans-serif;
    font-weight: 500;
    font-size: 39px;
    letter-spacing: 1px;
    color: var(--ivory);
  }
</style>
</head>
<body>
  <main class="label">
    <header class="maker">
      <span class="maker__line">FABBRICA LIQUORI</span>
      <span class="maker__name">F.lli CASTALDI</span>
    </header>

    <p class="tagline">AMARO DI CARATTERE</p>
    <h1 class="product-name">CARCIOFO</h1>

    <svg class="artichoke" viewBox="0 0 545 864" role="img" aria-label="Engraved-style illustration of an artichoke with purple-red top bracts, green lower leaves and stem">
      <defs>
        <linearGradient id="artichoke-tone" x1="0" y1="0" x2="0" y2="1">
          <stop offset="0" stop-color="#8e2e4e"/>
          <stop offset="0.28" stop-color="#8e2e4e"/>
          <stop offset="0.42" stop-color="#7f9e52"/>
          <stop offset="0.85" stop-color="#6a8a44"/>
          <stop offset="1" stop-color="#4d6a34"/>
        </linearGradient>
      </defs>
      <rect width="545" height="864" rx="40" fill="url(#artichoke-tone)" opacity="0.85"/>
    </svg>

    <footer class="origin-band">
      <p class="origin-band__text">BASSANO DEL GRAPPA / EST. 1886</p>
    </footer>
  </main>
</body>
</html>
```